Harbor Crest Renewal Business Cards

We need a sleek and sexy business card design

Contact Information for Business Card

Name, address, phone number, email. Martin DeSolva 482 Bramble Court Suite 200C Cedarvale NY 11958 (631)584-2276 Also a second version with the name Derek Hollis

```html
<!DOCTYPE html>
<html lang="en">
<head>
<meta charset="utf-8">
<title>Harbor Crest Renewal Business Cards</title>
<link rel="stylesheet" href="https://fonts.googleapis.com/css2?family=Montserrat:wght@700&family=Quicksand:wght@400&display=swap">
<style>
  :root {
    --brand-orange: #cf3d06;
    --brand-blue: #0a4590;
    --ink: #2b2b2b;
    --card-light: #ffffff;
    --card-shade: #dedede;
    --page-light: #f6f6f6;
    --page-shade: #dadada;
  }
  * { margin: 0; padding: 0; box-sizing: border-box; }
  html, body { width: 1200px; height: 1200px; overflow: hidden; }
  body {
    position: relative;
    background: radial-gradient(circle at 50% 45%, var(--page-light) 0%, var(--page-shade) 100%);
    font-family: "Quicksand", sans-serif;
  }
  .card {
    position: absolute;
    left: 276px;
    width: 648px;
    height: 370px;
    overflow: hidden;
    background: radial-gradient(ellipse at 35% 35%, var(--card-light) 30%, var(--card-shade) 100%);
    box-shadow: 4px 6px 8px rgba(0,0,0,0.25);
  }
  .card--front { top: 0; }
  .card--derek { top: 411px; }
  .card--martin { top: 830px; }
  .card__decor { position: absolute; inset: 0; width: 648px; height: 370px; }
  .brand-name {
    position: absolute;
    font-family: "Montserrat", sans-serif;
    font-weight: 700;
    color: var(--brand-blue);
    white-space: nowrap;
    transform: translate(-50%, -50%);
    text-align: center;
  }
  .card--front .brand-name { left: 323px; top: 200px; font-size: 34px; }
  .card--contact .brand-name { left: 148px; top: 200px; font-size: 19px; }
  .person-name {
    position: absolute;
    left: 303px;
    top: 64px;
    font-family: "Montserrat", sans-serif;
    font-weight: 700;
    font-size: 28px;
    color: #fff;
    line-height: 36px;
    white-space: nowrap;
  }
  .person-name--martin { left: 309px; }
  .contact-list { position: absolute; left: 287px; top: 0; list-style: none; }
  .contact-item {
    position: absolute;
    left: 0;
    display: flex;
    align-items: center;
    width: 345px;
  }
  .contact-item svg { width: 40px; height: 40px; flex: none; }
  .contact-item span {
    margin-left: 13px;
    font-size: 15px;
    line-height: 18px;
    color: var(--ink);
    white-space: nowrap;
  }
  .contact-item--phone { top: 158px; }
  .contact-item--address { top: 215px; }
  .contact-item--email { top: 272px; }
</style>
</head>
<body>

<svg width="0" height="0" style="position:absolute">
  <defs>
    <g id="card-corners">
      <path d="M0 0 H112 C60 30 20 80 0 130 Z" fill="var(--brand-blue)"/>
      <path d="M0 0 H84 C45 30 15 70 0 112 Z" fill="var(--brand-orange)"/>
      <path d="M648 239 C620 300 580 345 535 370 H648 Z" fill="var(--brand-blue)"/>
      <path d="M648 265 C625 315 600 345 563 370 H648 Z" fill="var(--brand-orange)"/>
    </g>
    <g id="name-band">
      <path d="M306 64 L648 50 V94 L306 106 A21 21 0 0 1 306 64 Z" fill="var(--brand-blue)"/>
      <path d="M306 60 L648 50 V88 L306 100 A20 20 0 0 1 306 60 Z" fill="var(--brand-orange)"/>
    </g>
    <g id="icon-phone">
      <circle cx="20" cy="20" r="20" fill="var(--brand-orange)"/>
      <path d="M25 11 C18 12 12 19 12 27 L17 28 L18 24 L16 22 C17 19 19 17 22 16 L24 18 L28 17 Z" fill="#fff"/>
    </g>
    <g id="icon-map">
      <circle cx="20" cy="20" r="20" fill="var(--brand-orange)"/>
      <path d="M12 12 L17 10 L23 12 L28 10 V28 L23 30 L17 28 L12 30 Z M17 13 V26 M23 15 V27" fill="none" stroke="#fff" stroke-width="3" stroke-linejoin="round"/>
    </g>
    <g id="icon-mail">
      <circle cx="20" cy="20" r="20" fill="var(--brand-orange)"/>
      <rect x="10" y="13" width="20" height="14" rx="1.5" fill="#fff"/>
      <path d="M10.5 14 L20 21 L29.5 14" fill="none" stroke="var(--brand-orange)" stroke-width="2"/>
    </g>
  </defs>
</svg>

<section class="card card--front">
  <svg class="card__decor" viewBox="0 0 648 370"><use href="#card-corners"/></svg>
  <p class="brand-name">Harbor Crest Renewal</p>
</section>

<section class="card card--contact card--derek">
  <svg class="card__decor" viewBox="0 0 648 370"><use href="#card-corners"/><use href="#name-band"/></svg>
  <p class="brand-name">Harbor Crest Renewal</p>
  <h2 class="person-name">Derek Hollis</h2>
  <ul class="contact-list">
    <li class="contact-item contact-item--phone">
      <svg viewBox="0 0 40 40"><use href="#icon-phone"/></svg>
      <span>(631) 584-2276</span>
    </li>
    <li class="contact-item contact-item--address">
      <svg viewBox="0 0 40 40"><use href="#icon-map"/></svg>
      <span>482 Bramble Court Suite 200C<br>Cedarvale NY 11958</span>
    </li>
    <li class="contact-item contact-item--email">
      <svg viewBox="0 0 40 40"><use href="#icon-mail"/></svg>
      <span>office@harborcrestrenewal.net</span>
    </li>
  </ul>
</section>

<section class="card card--contact card--martin">
  <svg class="card__decor" viewBox="0 0 648 370"><use href="#card-corners"/><use href="#name-band"/></svg>
  <p class="brand-name">Harbor Crest Renewal</p>
  <h2 class="person-name person-name--martin">Martin DeSolva</h2>
  <ul class="contact-list">
    <li class="contact-item contact-item--phone">
      <svg viewBox="0 0 40 40"><use href="#icon-phone"/></svg>
      <span>(631) 584-2276</span>
    </li>
    <li class="contact-item contact-item--address">
      <svg viewBox="0 0 40 40"><use href="#icon-map"/></svg>
      <span>482 Bramble Court Suite 200C<br>Cedarvale NY 11958</span>
    </li>
    <li class="contact-item contact-item--email">
      <svg viewBox="0 0 40 40"><use href="#icon-mail"/></svg>
      <span>office@harborcrestrenewal.net</span>
    </li>
  </ul>
</section>

</body>
</html>
```